Business Card Design job - Tyre Shop

Client wants a double sided business cards designed for a Tyre Shop.

The logo can be used in multiple ways, some examples are attached.

The reference font is:
https://www.typebarrow.com/fonts/open-sans
Others can be applied.

Color scheme should be mainly black and white, and red as a third less used color.

Contact Information for Business Card

Required Fields (Portuguese language):
- Name "Augusto Melro"
- Title "Gerente"
- Phone "253 704 862"
- Website "www.rodaslume.pt"
- Email "geral@rodaslume.pt
- Address "Rua da Fonteira N.187
4730-512 Cortelha, Vale Alvo"

Font styles to use
Sans Serif

Requirements
Must have
• Corporate Logo
Nice to have
• The client would like the card to have special feature to measure the tyre tread, as shown in examples attached.
• The tread Values as Portuguese law are:
• - Ilegal - less than 1.6mm
• - change tyres - between 3mm and 1.6 mm
• - OK - above 3mm
• Card should be kept standard rectangle size 85x55mm

```html
<!DOCTYPE html>
<html lang="pt">
<head>
<meta charset="utf-8">
<title>Rodas Lume – Cartão de Visita</title>
<link rel="stylesheet" href="https://fonts.googleapis.com/css2?family=Open+Sans:wght@400;600;700;800&family=Montserrat:wght@700&display=swap">
<style>
  :root {
    --card-black: #000000;
    --ink-white: #ffffff;
    --ink-grey: #bdbdbd;
    --stage: #e4e4e6;
    --alert-red: #e0161b;
    --alert-yellow: #f2d21b;
    --ok-green: #2fb82a;
  }
  * { margin: 0; padding: 0; box-sizing: border-box; }
  html, body {
    width: 1200px; height: 800px; overflow: hidden;
    background: var(--stage);
    font-family: "Open Sans", sans-serif;
  }
  .canvas { position: relative; width: 1200px; height: 800px; }

  .card {
    position: absolute;
    background: var(--card-black);
    color: var(--ink-white);
    overflow: hidden;
    box-shadow: 0 10px 30px rgba(0,0,0,.25);
  }

  /* Front: vertical side with tread gauge */
  .card-front { left: 220px; top: 168px; width: 300px; height: 464px; }
  .brand-name {
    font-family: "Open Sans", sans-serif;
    font-weight: 800;
    color: var(--ink-white);
    text-transform: uppercase;
    line-height: .95;
    letter-spacing: -0.5px;
  }
  .card-front .brand-name { position: absolute; left: 28px; top: 30px; font-size: 34px; }
  .website {
    position: absolute; left: 0; right: 0; top: 268px;
    text-align: center; font-size: 14px; color: var(--ink-white);
  }
  .tread-gauge { position: absolute; left: 0; bottom: 0; width: 300px; height: 140px; }
  .tread-gauge text { font-family: "Open Sans", sans-serif; fill: var(--ink-white); font-size: 10px; }

  /* Back: horizontal side with contacts */
  .card-back { left: 600px; top: 250px; width: 464px; height: 300px; }
  .card-back .brand-name {
    position: absolute; left: 40px; top: 90px; width: 160px;
    font-size: 26px; text-align: center;
  }
  .divider {
    position: absolute; left: 232px; top: 38px; width: 2px; height: 200px;
    background: var(--ink-white);
  }
  .person { position: absolute; left: 262px; top: 40px; }
  .person-name { font-family: "Montserrat", sans-serif; font-weight: 700; font-size: 18px; }
  .person-role { font-size: 10px; color: var(--ink-grey); margin-top: 1px; }
  .contacts { position: absolute; left: 262px; top: 132px; list-style: none; }
  .contacts li {
    display: flex; align-items: center; gap: 8px;
    font-size: 10.5px; line-height: 1.2; margin-bottom: 6px;
  }
  .contacts svg { width: 14px; height: 14px; flex: none; fill: none; stroke: var(--ink-white); stroke-width: 1.6; }
  .tagline {
    position: absolute; left: 0; right: 0; bottom: 22px;
    text-align: center; font-size: 9.5px; font-weight: 700;
    letter-spacing: 3.4px; text-transform: uppercase;
  }
</style>
</head>
<body>
<main class="canvas">

  <section class="card card-front" aria-label="Frente do cartão com medidor de piso">
    <div class="brand-name">Rodas<br>Lume</div>
    <p class="website">www.rodaslume.pt</p>

    <svg class="tread-gauge" viewBox="0 0 300 140" aria-label="Medidor de profundidade do piso">
      <!-- illegal -->
      <text x="22" y="14">ilegal</text>
      <polygon points="34,22 46,44 22,44" fill="none" stroke="var(--alert-red)" stroke-width="2"/>
      <text x="31" y="41" font-size="10" style="fill:var(--alert-red)">×</text>
      <line x1="34" y1="66" x2="34" y2="100" stroke="var(--alert-red)" stroke-dasharray="2 3"/>
      <text x="22" y="60">&lt;1,6</text>
      <!-- change -->
      <text x="66" y="14">trocar</text>
      <polygon points="80,22 92,44 68,44" fill="none" stroke="var(--alert-yellow)" stroke-width="2"/>
      <text x="78" y="41" font-size="10" font-weight="700" style="fill:var(--alert-yellow)">!</text>
      <line x1="80" y1="66" x2="80" y2="100" stroke="var(--alert-yellow)" stroke-dasharray="2 3"/>
      <text x="68" y="60">&lt;3,0</text>
      <!-- scale -->
      <text x="120" y="96">mm</text>
      <line x1="0" y1="102" x2="300" y2="102" stroke="var(--ink-white)" stroke-width="1"/>
      <!-- ok -->
      <rect x="246" y="58" width="20" height="18" rx="3" fill="none" stroke="var(--ok-green)" stroke-width="1.8"/>
      <polyline points="250,67 255,72 262,62" fill="none" stroke="var(--ok-green)" stroke-width="2"/>
      <text x="244" y="92">8,0</text>
      <line x1="256" y1="102" x2="256" y2="140" stroke="var(--ok-green)" stroke-width="2.5"/>
    </svg>
  </section>

  <section class="card card-back" aria-label="Verso do cartão com contactos">
    <div class="brand-name">Rodas<br>Lume</div>
    <div class="divider"></div>

    <div class="person">
      <p class="person-name">Augusto Melro</p>
      <p class="person-role">Gerente</p>
    </div>

    <ul class="contacts">
      <li>
        <svg viewBox="0 0 14 14"><rect x="4" y="1" width="6" height="12" rx="1"/><line x1="6" y1="11" x2="8" y2="11"/></svg>
        253 704 862
      </li>
      <li>
        <svg viewBox="0 0 14 14"><rect x="1" y="3" width="12" height="8"/><polyline points="1,3 7,8 13,3"/></svg>
        geral@rodaslume.pt
      </li>
      <li>
        <svg viewBox="0 0 14 14"><polyline points="1,7 7,2 13,7"/><polyline points="3,6 3,12 11,12 11,6"/><rect x="6" y="8" width="2" height="4"/></svg>
        <span>Rua da Fonteira N.187<br>4730-512 Cortelha, Vale Alvo</span>
      </li>
    </ul>

    <p class="tagline">Especialista em pneus &amp; manutenção automóvel</p>
  </section>

</main>
</body>
</html>
```